Lantern Harvest CD design

I need a CD cover & sleeve design for an upcoming February 2014 CD release event (at a music store). This is a collection of original songs written and sung by yours truly. Many songs are inspired by my ancestors, although there are a few songs that are just about life and love. We are all a product of our ancestry, and we carry this history in our hearts whether we think it influences us or not. This is my first CD although I've been singing and performing for over 30 years, and this body of work is where I'm at now musically and creatively. I'm proud of the effort I've made and want to present myself as someone who is real and genuine. My design style tends towards simple, clean, uncluttered lines, sans serif type faces. No loud or saturated colors please, no reds or pinks. I love the blues & greens. I have a sepia image in my head, but maybe because I've been looking at old photos of my grandparents as inspiration for the last 6 months...!

I am including two shots of me, and some old photos that could be used as a design element, but not mandatory. I wanted you to have some choices... I also have a lot of CD liner notes, but am willing to edit if I need to. This would need to be in 4 color with a sleeve that flaps open, and a lift of something similar for CD imprint. Sorry about the tight deadline, I have to get a print run done before the launch and that lead time is ridiculously tight. If you want an mp3 sample of one song I am happy to forward to give you an idea of my sound, it might help to inspire if you're a music person :-) just let me know at megtalvinatpostvellidotcom

Update for inside text: Cover photo by Daniel Kopreth, others photos taken by Meg Talvin.

Target Market(s)

Anyone who likes original singer / songwriter music, fellow music lovers, audience members after a performance. My influence is only in the northeast US thus far.

Industry/Entity Type

Store

Requirements
Must have
• Title of CD: Lantern Harvest

Name: Meg Talvin

lower left back corner - leave 1-1/4"x1/2" room in design on back cover for UPC barcode
Nice to have
• A lighter touch, artistic vibe, softer painterly approach, Don't mind the blue / green spectrum, or a sepia toned feel. Some music folks feedback has inspired me to update this: I need o have my face on the cover! the b&w shot is a little better. And it would be nice to incorporate both sets of ancestor pictures in some way. (The faded grandma and young boy and the couple with flowers that I am holding).
Song list on the back is helpful, too.
Should not have
• No loud, saturated colors, no reds or pinks please.

```html
<!DOCTYPE html>
<html lang="en">
<head>
<meta charset="utf-8">
<title>Lantern Harvest – Back Cover</title>
<link rel="stylesheet" href="https://fonts.googleapis.com/css2?family=Cabin:wght@400;500;600;700&display=swap">
<style>
  :root {
    --page: #d9d9d9;
    --cover-light: #e6ecea;
    --cover-mid: #d3dcda;
    --cover-deep: #bccac8;
    --ink: #3b4244;
    --ink-soft: #4a5254;
  }
  * { box-sizing: border-box; margin: 0; padding: 0; }
  html, body {
    width: 1200px; height: 923px; overflow: hidden;
    background: var(--page);
    font-family: "Cabin", sans-serif;
    color: var(--ink);
  }
  .back-cover {
    position: absolute; left: 162px; top: 47px;
    width: 875px; height: 828px;
    overflow: hidden;
  }
  .cover-texture {
    position: absolute; inset: 0;
    background:
      radial-gradient(circle at 78% 22%, rgba(255,255,255,0.55) 0, rgba(255,255,255,0) 30%),
      radial-gradient(circle at 20% 70%, rgba(255,255,255,0.35) 0, rgba(255,255,255,0) 35%),
      linear-gradient(160deg, var(--cover-light) 0%, var(--cover-mid) 55%, var(--cover-deep) 100%);
  }
  .liner-quote {
    position: absolute; left: 117px; top: 80px; width: 662px;
    font-size: 13.5px; line-height: 22px; font-weight: 500;
    color: var(--ink-soft);
  }
  .track-list {
    position: absolute; left: 117px; top: 206px;
    list-style: none;
  }
  .track {
    height: 43px; display: flex; align-items: baseline; white-space: nowrap;
  }
  .track-title {
    font-size: 27px; font-weight: 600; color: var(--ink);
  }
  .track-credit {
    font-size: 14px; font-weight: 400; color: var(--ink-soft); margin-left: 9px;
  }
  .credits {
    position: absolute; left: 117px; top: 650px; width: 620px;
    font-size: 12.5px; line-height: 20px; font-weight: 600; color: var(--ink-soft);
  }
  .credits p { margin-bottom: 7px; }
</style>
</head>
<body>
  <section class="back-cover">
    <div class="cover-texture" role="img" aria-label="Soft pale blue-grey painterly texture with faint snowy bokeh"></div>

    <p class="liner-quote">"Lorem ipsum dolor sit amet, consectetur adipisicing elit, sed do eiusmod tempor incididunt ut labore et dolore magna aliqua. Ut enim ad minim veniam, quis nostrud exercitation ullamco laboris nisi ut aliquip ex ea commodo consequat. Duis aute irure dolor in reprehenderit in voluptate velit esse cillum dolore eu fugiat nulla pariatur. Excepteur sint occaecat cupidatat non proident, sunt in culpa qui officia deserunt mollit anim id est laborum."</p>

    <ol class="track-list">
      <li class="track"><span class="track-title">1) Morning Road</span><span class="track-credit">&nbsp;(text: Marwick, music: Tessaro)</span></li>
      <li class="track"><span class="track-title">2) Long Way Round Blues</span><span class="track-credit">(text: Marwick, music: Tessaro)</span></li>
      <li class="track"><span class="track-title">3) River Girl</span><span class="track-credit">(text: Marwick, music: Tessaro)</span></li>
      <li class="track"><span class="track-title">4) Hold My Hand</span><span class="track-credit">(text: Marwick, music: Tessaro)</span></li>
      <li class="track"><span class="track-title">5) Rosewood</span><span class="track-credit">(text: Marwick, music: Tessaro)</span></li>
      <li class="track"><span class="track-title">6) Undertow</span><span class="track-credit">(text: Marwick, music: Tessaro)</span></li>
      <li class="track"><span class="track-title">7) Silly Heart</span><span class="track-credit">(text: Marwick, music: Tessaro)</span></li>
      <li class="track"><span class="track-title">8) Stay Awhile</span><span class="track-credit">(text: Marwick, music: Tessaro)</span></li>
      <li class="track"><span class="track-title">9) Rain is Falling</span><span class="track-credit">(text: Marwick, music: Tessaro)</span></li>
      <li class="track"><span class="track-title">10) Sweet Rosie</span><span class="track-credit">(text: Marwick, music: Tessaro)</span></li>
    </ol>

    <div class="credits">
      <p>Recorded at Gray Heron Sound, Alder Falls, VT</p>
      <p>www.grayheronsound.com, and at Colin Aveshaw Studio in Marrow Point, ME.&nbsp; Mixed by Colin Aveshaw, Marrow Point, ME &amp; Lakeford, MI</p>
      <p>Photography by Daniel Kopreth</p>
      <p>Sweet Rosie written by Hollis Crane &amp; Arthur Vell 1928</p>
      <p>© Original lyrics and music by Meg Talvin 2013</p>
    </div>
  </section>
</body>
</html>
```